Business Folder

I need a fresh, modern design for a business folder. I have our company's colors, logo, and a separate file for just the graphic part of our logo as a design element. No photo, just colors, gradients, and shadows to create depth. I like the idea of a rich grey as the background, however, I realize we'd have to lighten to 'Tax Advisory Services' part of our logo.

The design would just be the 'front' or outside of the folder from Zelvora. Design file attached. You can find that here under 9 x 12 standard folder, Left and Right Pockets With Slit Both Sides:

https://www.zelvora-example.com/content.html?id=folderDownloadTemplates&rightMenuId=rightMenu&footerId=bodyFooterStyle6

```html
<!DOCTYPE html>
<html lang="en">
<head>
<meta charset="utf-8">
<title>Lumora Tax Advisory – Presentation Folder</title>
<link href="https://fonts.googleapis.com/css2?family=Montserrat:wght@200;400;500;600;900&display=swap" rel="stylesheet">
<style>
  :root {
    --stage: #8a8a8a;
    --paper: #ffffff;
    --navy: #0d4a7a;
    --deep: #0a5289;
    --blue: #0290d4;
    --sky: #5bc3e8;
    --haze: #dbe9f6;
    --lilac: #c9cfea;
    --ink: #4a4a4a;
    --spine: #b9b9b9;
  }
  * { box-sizing: border-box; margin: 0; padding: 0; }
  html, body { width: 1200px; height: 1200px; overflow: hidden; }
  body {
    background: var(--stage);
    font-family: "Montserrat", sans-serif;
    position: relative;
  }
  .sheet {
    position: absolute;
    left: 210px;
    width: 780px;
    height: 520px;
    display: flex;
    box-shadow: 0 6px 18px rgba(0,0,0,.35);
  }
  .sheet--outside { top: 40px; }
  .sheet--inside { top: 620px; }
  .panel {
    position: relative;
    width: 390px;
    height: 520px;
    background: var(--paper);
    overflow: hidden;
  }

  /* shared top wash */
  .wash {
    position: absolute; left: 0; top: 0; width: 100%; height: 60%;
    background:
      radial-gradient(ellipse at 80% 0%, rgba(201,207,234,.85), transparent 60%),
      radial-gradient(ellipse at 20% 10%, rgba(168,210,240,.6), transparent 55%),
      linear-gradient(180deg, var(--haze) 0%, rgba(255,255,255,0) 100%);
  }
  .edge-band {
    position: absolute; left: 0; bottom: 0; width: 100%; height: 18px;
    background: var(--blue);
  }

  /* front cover */
  .brand {
    position: absolute; left: 36px; top: 58px;
    display: flex; align-items: center; gap: 10px;
    font-weight: 600; font-size: 34px; letter-spacing: 1px;
    color: var(--navy);
  }
  .brand__mark { width: 16px; height: 16px; background: var(--navy); }
  .headline { position: absolute; left: 36px; top: 190px; }
  .headline__lead { font-weight: 200; font-size: 38px; color: var(--ink); line-height: 1.1; }
  .headline__main { font-weight: 900; font-size: 40px; color: var(--navy); line-height: 1.1; letter-spacing: 1px; }
  .headline__sub { margin-top: 12px; font-size: 14px; color: var(--ink); line-height: 1.35; }
  .cover-url { position: absolute; left: 36px; bottom: 42px; font-size: 11px; color: var(--ink); }
  .cover-graphic {
    position: absolute; right: 0; top: 170px; width: 150px; height: 332px;
    background: linear-gradient(160deg, var(--sky) 0%, var(--blue) 45%, var(--deep) 100%);
    clip-path: polygon(60% 0, 100% 0, 100% 100%, 0 100%);
  }

  /* inside spread */
  .inside-left { background: var(--paper); }
  .inside-right { background: linear-gradient(90deg, var(--spine) 0%, #e6e6e6 40%, var(--paper) 75%); }
  .ghost-name {
    position: absolute; top: 250px; width: 100%; text-align: center;
    font-weight: 600; font-size: 56px; color: rgba(0,0,0,.05);
  }
  .pocket {
    position: absolute; bottom: 0; height: 200px; width: 380px;
    display: flex; align-items: center; justify-content: center;
    color: var(--paper);
  }
  .pocket--left {
    left: 0;
    border-top-right-radius: 14px;
    background: linear-gradient(135deg, #4ab0e0 0%, var(--blue) 55%, #1a8fd0 100%);
    clip-path: polygon(0 0, 97% 0, 100% 100%, 0 100%);
  }
  .pocket--right {
    right: 0;
    border-top-left-radius: 14px;
    background: var(--blue);
    clip-path: polygon(3% 0, 100% 0, 100% 100%, 0 100%);
  }
  .pocket__url { font-size: 19px; letter-spacing: .5px; }
  .pocket__brand {
    display: flex; align-items: center; gap: 12px;
    font-weight: 600; font-size: 44px; letter-spacing: 1px;
  }
  .pocket__brand .brand__mark { width: 20px; height: 20px; background: var(--paper); }
</style>
</head>
<body>

  <section class="sheet sheet--outside" aria-label="Folder outside">
    <div class="panel back-cover">
      <div class="wash" role="img" aria-label="Soft faceted blue crystal pattern fading into white"></div>
      <div class="edge-band"></div>
    </div>
    <div class="panel front-cover">
      <div class="wash" role="img" aria-label="Soft faceted blue crystal pattern fading into white"></div>
      <div class="brand"><span class="brand__mark"></span>Lumora</div>
      <div class="headline">
        <p class="headline__lead">Committed to</p>
        <p class="headline__main">SOLUTIONS</p>
        <p class="headline__sub">A Present And Future<br>Business Service</p>
      </div>
      <div class="cover-graphic" role="img" aria-label="Large blue brand graphic element"></div>
      <p class="cover-url">www.lumorataxadvisory.com</p>
      <div class="edge-band"></div>
    </div>
  </section>

  <section class="sheet sheet--inside" aria-label="Folder inside with pockets">
    <div class="panel inside-left">
      <p class="ghost-name">Lumora</p>
      <div class="pocket pocket--left" role="img" aria-label="Blue faceted pattern pocket">
        <span class="pocket__url">www.lumorataxadvisory.com</span>
      </div>
    </div>
    <div class="panel inside-right">
      <p class="ghost-name">Lumora</p>
      <div class="pocket pocket--right">
        <span class="pocket__brand"><span class="brand__mark"></span>Lumora</span>
      </div>
    </div>
  </section>

</body>
</html>
```